Business card design needed for Renewable utilities company based in New Zealand.

We supply and install solar panels and all components along with it for a fully customisable PV system that helps customer save money on their energy bills right away and also save the planet!

I have attached logo & website design files to give you a better insight.

Industry/Entity Type

Business

```html
<!DOCTYPE html>
<html lang="en">
<head>
<meta charset="utf-8">
<title>Solvane Energy – Business Card</title>
<link rel="stylesheet" href="https://fonts.googleapis.com/css2?family=Open+Sans:wght@300;400;600&display=swap">
<style>
  :root {
    --page-bg: #e9e9e7;
    --card-white: #f2f2f2;
    --navy-deep: #0d2a55;
    --navy-mid: #1a4a85;
    --brand-blue: #1e8fd6;
    --ink: #2b2b2b;
    --ink-soft: #555555;
    --white: #ffffff;
  }
  * { box-sizing: border-box; margin: 0; padding: 0; }
  html, body {
    width: 1200px;
    height: 900px;
    overflow: hidden;
    background: var(--page-bg);
    font-family: "Open Sans", Arial, sans-serif;
  }
  .canvas {
    position: relative;
    width: 1200px;
    height: 900px;
  }
  .card {
    position: absolute;
    top: 296px;
    width: 540px;
    height: 309px;
    border-radius: 3px;
    box-shadow: 0 6px 18px rgba(0,0,0,0.18);
    overflow: hidden;
  }

  /* Back of card */
  .card-back {
    left: 40px;
    background: radial-gradient(ellipse at 50% 40%, var(--navy-mid) 0%, var(--navy-deep) 80%);
    color: var(--white);
  }
  .card-back .map-texture {
    position: absolute;
    inset: 30px 40px;
    border-radius: 40px;
    background: radial-gradient(ellipse at center, rgba(255,255,255,0.06), rgba(255,255,255,0) 70%);
  }
  .back-brand {
    position: absolute;
    left: 0; right: 0;
    top: 92px;
    display: flex;
    flex-direction: column;
    align-items: center;
  }
  .brand-dot-light {
    width: 58px; height: 58px;
    border-radius: 50%;
    background: #e3e6ea;
    margin-bottom: 14px;
  }
  .back-brand .brand-name {
    font-size: 30px;
    font-weight: 400;
    color: var(--white);
    letter-spacing: 0.5px;
  }
  .back-url {
    position: absolute;
    left: 0; right: 0;
    bottom: 48px;
    text-align: center;
    font-size: 13px;
    font-weight: 300;
    letter-spacing: 0.4px;
    color: #d9e3f0;
  }

  /* Front of card */
  .card-front {
    left: 620px;
    background: var(--card-white);
    color: var(--ink);
  }
  .front-brand {
    position: absolute;
    left: 34px;
    top: 118px;
    width: 220px;
    display: flex;
    flex-direction: column;
    align-items: center;
  }
  .brand-dot-dark {
    width: 62px; height: 62px;
    border-radius: 50%;
    background: linear-gradient(160deg, var(--brand-blue), var(--navy-deep));
    margin-bottom: 12px;
  }
  .front-brand .brand-name {
    font-size: 25px;
    font-weight: 400;
    color: var(--brand-blue);
    white-space: nowrap;
  }
  .contact-block {
    position: absolute;
    left: 290px;
    top: 46px;
    width: 220px;
  }
  .person-name {
    font-size: 18px;
    font-weight: 400;
    letter-spacing: 0.6px;
    text-transform: uppercase;
    color: var(--ink);
  }
  .person-role {
    font-size: 11px;
    font-weight: 400;
    color: var(--ink-soft);
    margin-top: 2px;
    padding-left: 22px;
  }
  .rule {
    border: 0;
    border-top: 1px dotted var(--brand-blue);
    margin: 12px 0 14px;
  }
  .contact-list {
    list-style: none;
    font-size: 12px;
    font-weight: 400;
    line-height: 19px;
  }
  .contact-list li { display: flex; }
  .contact-label {
    width: 22px;
    font-weight: 600;
    color: var(--brand-blue);
  }
  .address {
    font-style: normal;
    font-size: 12px;
    line-height: 19px;
    margin-top: 8px;
    padding-left: 22px;
  }
</style>
</head>
<body>
  <main class="canvas">
    <section class="card card-back" aria-label="Card back">
      <div class="map-texture" role="img" aria-label="Faint dotted world map pattern"></div>
      <div class="back-brand">
        <span class="brand-dot-light"></span>
        <span class="brand-name">Solvane Energy</span>
      </div>
      <p class="back-url">www.solvaneenergy.com</p>
    </section>

    <section class="card card-front" aria-label="Card front">
      <div class="front-brand">
        <span class="brand-dot-dark"></span>
        <span class="brand-name">Solvane Energy</span>
      </div>
      <div class="contact-block">
        <h1 class="person-name">Maren Holloway</h1>
        <p class="person-role">Manager</p>
        <hr class="rule">
        <ul class="contact-list">
          <li><span class="contact-label">M</span>555 014 2387</li>
          <li><span class="contact-label">T</span>555 018 6604</li>
          <li><span class="contact-label">E</span>holloway@solvaneenergy.com</li>
        </ul>
        <address class="address">
          1270 Harbour Lane<br>
          Suite 140<br>
          Riverton, CA 90210
        </address>
      </div>
    </section>
  </main>
</body>
</html>
```